Infographic of the benefits of varying cannabinoids. Should be in SVG format with clickable links.

Our company sells cannabinoid products online, primarily tinctures of various CBD derivative blends. We need an infographic built which we will use on a landing page. I have attached a copy of our draft logo which should be incorporated into the infographic, but feel free to take some creative liberty with what I've provided.. The color scheme on the design should be appropriate for an earthy / planty product. Probably greens and light brown.

I have a list of desired effects and the different cannabinoids which will trigger said effect. The infographic should have a flow feel to it where readers will scroll through desired effects to see the cannabinoid which produces / impacts it.

The image needs to be in SVG format so that it loads quickly, can be SEO optimized, and have clickable segments built into the image. The clickable pieces of the image should in some way have a visual queue that will guide people to click or tap to open the link (which we will generally be linking to a product).

Each desired effect (pain management, insomnia, etc), and each cannabinoid, needs to be clickable within the SVG using markup.

For example,
- Anxiety - link which we will swap out for CBD/CBG product on our site
--- CBD - link which we will swap out for CBD product link on our site
--- CBG - link which we will swap out for CBG product link on our site

Here is the full list of groupings, symptoms, and mapped cannabinoids that need to be built into the infographic. Where links are present to FBWS.org, there should be a visual queue that there is a backing study from the Federal Bureau for Wellness Studies (FBWS) which is a clickable link to the FBWS study referenced.

- COVID Symptoms & Prevention
https://studies.medlorix.org/48120563/
-- CBGA
-- CBDA
- Pain
https://www.medlorix.org/archive/papers/QX7140285/ (pain management)
https://www.medlorix.org/archive/papers/QX7391046/ (chronic pain dosage)
-- Cramps / Migraine / Headache / Phantom Limb / Spinal Injury
--- CBD
--- THC
Fibromyalgia
--- CBD
--- CBN
--- THC
-- General Pain
--- CBC
--- CBD
--- CBN
--- THC
--- THCv
-- Arthritis / Inflammation
https://www.medlorix.org/studies/41730297 (arthritis)
https://www.medlorix.org/archive/papers/QX7391046/ (inflammation)
--- CBC
--- CBD
--- CBDa
--- CBG
--- CBN
--- THC
--- THCa
- Sleep
-- Insomnia
https://www.medlorix.org/archive/papers/QX8264713/
--- CBC
--- CBD
--- CBN
--- THC
- Gastro
-- General Gastro / Nausea
https://www.medlorix.org/library/VRL630184/
--- CBD
--- THC
Crohn’s
https://www.medlorix.org/archive/papers/QX7815320/
--- CBD
--- THC
--- THCa
- Mood
-- Anxiety
https://www.medlorix.org/archive/papers/QX9037452/
--- CBD
--- CBG
-- ADHD / Stress
https://www.medlorix.org/studies/41962708
--- CBD
--- THC
--- PTSD
--- CBD
--- CBG
--- THC
-- Depression
https://studies.medlorix.org/39507186/
--- CBC
--- CBD
--- CBG
--- CBN
--- THC
- Neuro
-- Epilepsy / Seizures
https://www.medlorix.org/studies/42318590
--- CBD
--- CBN
--- THCa
--- THCv
-- Multiple Sclerosis
https://www.medlorix.org/archive/papers/QX8609135/
--- CBD
--- CBN
--- THC
--- THCa
-- Alzheimer’s
https://www.medlorix.org/studies/41245873
--- CBC
--- CBD
--- CBG
--- THC
--- THCa

Need extra days to review

CBD users who are looking for different cannabinoids based on health benefits.

Cannabis / Hemp

• SVG format with clickable links on the different benefits and on each cannabinoid.

```html
<!DOCTYPE html>
<html lang="en">
<head>
<meta charset="utf-8">
<title>Verdalis – Cannabinoid Benefits Chart</title>
<link href="https://fonts.googleapis.com/css2?family=Play:wght@400;700&display=swap" rel="stylesheet">
<style>
  :root{
    --green-bright:#72d04c;
    --green-mid:#4ea83b;
    --green-deep:#1f4d1f;
    --leaf-dark:#163a17;
    --chip:#6fd147;
    --chip-text:#f2fbe9;
    --bar:rgba(232,244,226,.62);
    --bar-text:#34422f;
    --orange:#f28a3a;
    --brand-text:#e9f6e1;
    --white:#ffffff;
  }
  *{box-sizing:border-box;margin:0;padding:0}
  html,body{width:1200px;height:863px;overflow:hidden}
  body{font-family:"Play",sans-serif;background:#f3f4f2}
  .canvas{position:relative;width:1200px;height:863px;overflow:hidden;
    background:linear-gradient(100deg,var(--green-bright) 0%,var(--green-mid) 38%,var(--green-deep) 62%,var(--leaf-dark) 100%)}
  .leaf-photo{position:absolute;left:560px;top:0;width:640px;height:863px;
    background:
      radial-gradient(ellipse 260px 200px at 60% 38%,rgba(90,150,60,.55),transparent 70%),
      radial-gradient(ellipse 220px 260px at 30% 70%,rgba(70,130,50,.45),transparent 70%),
      radial-gradient(ellipse 300px 180px at 85% 80%,rgba(40,90,35,.5),transparent 70%),
      linear-gradient(90deg,rgba(31,77,31,0) 0%,rgba(22,58,23,.6) 40%,rgba(18,48,20,.8) 100%)}
  .brand{position:absolute;right:110px;top:74px;display:flex;align-items:center;gap:10px;
    color:var(--brand-text);font-family:"Play",sans-serif;font-weight:700}
  .brand-dot{width:18px;height:18px;border-radius:50%;background:var(--chip)}
  .brand-name{font-size:28px;letter-spacing:1px;line-height:1}
  .chart{position:absolute;left:44px;top:118px;width:760px}
  .group{display:flex;align-items:center;margin-bottom:20px}
  .category{flex:0 0 200px;display:flex;align-items:center;text-decoration:none}
  .cat-icon{width:40px;height:40px;border-radius:50%;background:var(--orange);
    border:2px solid rgba(255,255,255,.55);flex:0 0 40px;position:relative;z-index:1}
  .cat-label{margin-left:-8px;padding:4px 14px 4px 16px;background:var(--chip);color:var(--white);
    font-weight:700;font-size:15px;font-variant:small-caps;border-radius:0 14px 14px 0;white-space:nowrap}
  .rows{display:flex;flex-direction:column;gap:8px}
  .row{display:inline-flex;align-items:center;height:28px;padding:0 6px 0 14px;background:var(--bar);
    border-radius:14px;text-decoration:none;width:max-content}
  .row-label{width:250px;font-size:12px;color:var(--bar-text);line-height:1.05}
  .row-label.small{font-size:10.5px}
  .chips{display:flex;gap:10px}
  .chip{display:inline-block;min-width:44px;height:18px;line-height:18px;padding:0 10px;border-radius:9px;
    background:var(--chip);color:var(--chip-text);font-size:11px;font-weight:700;text-align:center;text-decoration:none}
  .row.chips-only{padding-left:8px}
</style>
</head>
<body>
<main class="canvas">
  <div class="leaf-photo" role="img" aria-label="Close-up photograph of green hemp leaves"></div>

  <div class="brand">
    <span class="brand-dot"></span>
    <span class="brand-name">Verdalis</span>
  </div>

  <section class="chart">
    <div class="group">
      <a class="category" href="https://studies.medlorix.org/48120563/"><span class="cat-icon"></span><span class="cat-label">COVID Symptoms &amp; Prevention</span></a>
      <div class="rows" style="margin-left:40px">
        <div class="row chips-only"><span class="chips"><a class="chip" href="#">CBDA</a><a class="chip" href="#">CBGA</a></span></div>
      </div>
    </div>

    <div class="group">
      <a class="category" href="https://www.medlorix.org/archive/papers/QX7140285/"><span class="cat-icon"></span><span class="cat-label">Pain</span></a>
      <div class="rows">
        <a class="row" href="https://www.medlorix.org/archive/papers/QX7391046/"><span class="row-label small">Cramps / Migraine / Headache<br>Phantom Limb / Spinal Injury</span><span class="chips"><span class="chip">CBD</span><span class="chip">THC</span></span></a>
        <a class="row" href="#"><span class="row-label">Fibromyalgia</span><span class="chips"><span class="chip">CBD</span><span class="chip">CBN</span><span class="chip">THC</span></span></a>
        <a class="row" href="#"><span class="row-label">General Pain</span><span class="chips"><span class="chip">CBC</span><span class="chip">CBD</span><span class="chip">CBN</span><span class="chip">THC</span><span class="chip">THCv</span></span></a>
        <a class="row" href="https://www.medlorix.org/studies/41730297"><span class="row-label">Arthritis / Inflammation</span><span class="chips"><span class="chip">CBC</span><span class="chip">CBD</span><span class="chip">CBDa</span><span class="chip">CBG</span><span class="chip">CBN</span><span class="chip">THC</span><span class="chip">THCa</span></span></a>
      </div>
    </div>

    <div class="group">
      <a class="category" href="#"><span class="cat-icon"></span><span class="cat-label">Sleep</span></a>
      <div class="rows">
        <a class="row" href="https://www.medlorix.org/archive/papers/QX8264713/"><span class="row-label">Insomnia</span><span class="chips"><span class="chip">CBC</span><span class="chip">CBD</span><span class="chip">CBN</span><span class="chip">THC</span></span></a>
      </div>
    </div>

    <div class="group">
      <a class="category" href="#"><span class="cat-icon"></span><span class="cat-label">Gastro</span></a>
      <div class="rows">
        <a class="row" href="https://www.medlorix.org/library/VRL630184/"><span class="row-label">General Gastro / Nausea</span><span class="chips"><span class="chip">CBD</span><span class="chip">THC</span></span></a>
        <a class="row" href="https://www.medlorix.org/archive/papers/QX7815320/"><span class="row-label">Crohn’s</span><span class="chips"><span class="chip">CBD</span><span class="chip">THC</span><span class="chip">THCa</span></span></a>
      </div>
    </div>

    <div class="group">
      <a class="category" href="#"><span class="cat-icon"></span><span class="cat-label">Mood</span></a>
      <div class="rows">
        <a class="row" href="https://www.medlorix.org/archive/papers/QX9037452/"><span class="row-label">Anxiety</span><span class="chips"><span class="chip">CBD</span><span class="chip">CBG</span></span></a>
        <a class="row" href="https://www.medlorix.org/studies/41962708"><span class="row-label">ADHD / Stress</span><span class="chips"><span class="chip">CBD</span><span class="chip">THC</span></span></a>
        <a class="row" href="#"><span class="row-label">PTSD</span><span class="chips"><span class="chip">CBD</span><span class="chip">CBG</span><span class="chip">THC</span></span></a>
        <a class="row" href="https://studies.medlorix.org/39507186/"><span class="row-label">Depression</span><span class="chips"><span class="chip">CBC</span><span class="chip">CBD</span><span class="chip">CBG</span><span class="chip">CBN</span><span class="chip">THC</span></span></a>
      </div>
    </div>

    <div class="group">
      <a class="category" href="#"><span class="cat-icon"></span><span class="cat-label">Neuro</span></a>
      <div class="rows">
        <a class="row" href="https://www.medlorix.org/studies/42318590"><span class="row-label">Epilepsy / Seizures</span><span class="chips"><span class="chip">CBD</span><span class="chip">CBN</span><span class="chip">THCa</span><span class="chip">THCv</span></span></a>
        <a class="row" href="https://www.medlorix.org/archive/papers/QX8609135/"><span class="row-label">Multiple Sclerosis</span><span class="chips"><span class="chip">CBD</span><span class="chip">CBN</span><span class="chip">THC</span><span class="chip">THCa</span></span></a>
        <a class="row" href="https://www.medlorix.org/studies/41245873"><span class="row-label">Alzheimer’s</span><span class="chips"><span class="chip">CBC</span><span class="chip">CBD</span><span class="chip">CBG</span><span class="chip">THC</span><span class="chip">THCa</span></span></a>
      </div>
    </div>
  </section>
</main>
</body>
</html>
```